Webpage

I am a professional genealogist. I need a webpage that is professional looking (using the logo I chose), I can add hyperlinks and photos to if and when I want.

```html
<!DOCTYPE html>
<html lang="en">
<head>
<meta charset="utf-8">
<title>Heritage Line Research</title>
<link rel="stylesheet" href="https://fonts.googleapis.com/css2?family=Jost:wght@400;500&display=swap">
<style>
  :root {
    --teal: #1aa3b8;
    --mint: #d5e3dc;
    --ink: #2b2d31;
    --white: #ffffff;
    --card-body: #f5f7f6;
    --footer: #2f333b;
    --field-border: #9a9ea3;
  }
  * { box-sizing: border-box; margin: 0; padding: 0; }
  html, body { width: 1200px; height: 1000px; overflow: hidden; }
  body { font-family: "Jost", sans-serif; color: var(--ink); background: var(--mint); position: relative; }

  .site-header {
    position: absolute; top: 0; left: 0; width: 1200px; height: 143px;
    background: var(--white);
    border-top: 5px solid var(--mint);
    border-bottom: 5px solid var(--mint);
  }
  .brand {
    position: absolute; left: 104px; top: 5px; height: 128px;
    display: flex; align-items: center; gap: 16px;
  }
  .brand-mark { width: 88px; height: 88px; border-radius: 50%; background: var(--teal); }
  .brand-name { font-size: 30px; font-weight: 400; color: var(--ink); letter-spacing: -0.3px; }

  .main-nav { position: absolute; right: 99px; top: -5px; height: 143px; display: flex; gap: 0; }
  .main-nav a {
    display: block; height: 143px; line-height: 159px; padding: 0 15px;
    font-size: 19px; color: var(--ink); text-decoration: none;
    border-top: 5px solid transparent; border-bottom: 5px solid transparent;
  }
  .main-nav a.is-active { color: var(--teal); border-top-color: var(--teal); border-bottom-color: var(--teal); padding: 0 8px; width: 60px; text-align: center; }

  .hero {
    position: absolute; top: 143px; left: 0; width: 1200px; height: 450px;
    background: linear-gradient(180deg, #c9d0d2 0%, #aab4ae 40%, #7f8b76 62%, #a6ad94 100%);
  }

  .feature-card {
    position: absolute; top: 517px; width: 300px; height: 195px;
    border-top: 5px solid var(--teal); background: var(--card-body);
  }
  .feature-card:nth-of-type(1) { left: 100px; }
  .feature-card:nth-of-type(2) { left: 450px; }
  .feature-card:nth-of-type(3) { left: 800px; }
  .feature-card h2 {
    height: 71px; line-height: 76px; text-align: center;
    font-size: 33px; font-weight: 400; background: rgba(255,255,255,0.72);
  }
  .feature-card p { padding: 14px 18px 0 15px; font-size: 14px; line-height: 17px; text-align: justify; }
  .feature-card a { position: absolute; left: 15px; top: 157px; font-size: 14px; color: var(--teal); }
  .feature-card:nth-of-type(2) p, .feature-card:nth-of-type(2) a { padding-left: 18px; }
  .feature-card:nth-of-type(2) a { left: 18px; }
  .feature-card:nth-of-type(3) p { padding-left: 19px; }
  .feature-card:nth-of-type(3) a { left: 19px; }

  .site-footer { position: absolute; top: 797px; left: 0; width: 1200px; height: 203px; background: var(--footer); color: var(--white); }
  .footer-col { position: absolute; top: 18px; }
  .footer-col h3 { font-size: 33px; font-weight: 400; line-height: 40px; margin-bottom: 8px; }
  .contact-col { left: 100px; }
  .contact-col address { font-style: normal; font-size: 14.5px; line-height: 17px; }
  .contact-col a { color: var(--white); }
  .posts-col { left: 425px; }
  .posts-col ul { list-style: none; }
  .posts-col li { font-size: 14.5px; line-height: 17px; margin-bottom: 13px; }
  .posts-col a { color: var(--white); }
  .search-col { left: 777px; }
  .search-field {
    position: relative; width: 269px; height: 40px; margin-top: 8px;
    background: var(--white); border: 2px solid var(--field-border);
  }
  .search-field svg { position: absolute; right: 6px; top: 6px; }
</style>
</head>
<body>
  <header class="site-header">
    <div class="brand">
      <span class="brand-mark"></span>
      <span class="brand-name">Heritage Line Research</span>
    </div>
    <nav class="main-nav">
      <a class="is-active" href="#">About</a>
      <a href="#">Services</a>
      <a href="#">Contact</a>
      <a href="#">Publications</a>
      <a href="#">Blog</a>
      <a href="#">Links</a>
    </nav>
  </header>

  <div class="hero" role="img" aria-label="Photo of a smiling grandfather and granddaughter in a sunny meadow with trees behind"></div>

  <section class="feature-card">
    <h2>About Us</h2>
    <p>Dana Whitfield is a professional genealogist who has x amount of years of experience in research and analysis in the state of Texas.</p>
    <a href="#">Learn more about us...</a>
  </section>
  <section class="feature-card">
    <h2>Services</h2>
    <p>Our services include forensic genealogy, kinship determination, research analysis and consultation, record retrieval, and more.</p>
    <a href="#">See all of our services...</a>
  </section>
  <section class="feature-card">
    <h2>Publications</h2>
    <p>Dana Whitfield’s published works include (brief description and teaser on publications goes here...)</p>
    <a href="#">Read our publications...</a>
  </section>

  <footer class="site-footer">
    <div class="footer-col contact-col">
      <h3>Contact</h3>
      <address>
        Heritage Line Research<br>
        Dana Whitfield, Professional Genealogist<br>
        PO Box 4471<br>
        Maple Falls, TX 78990-4471<br>
        555-201-4478<br>
        <a href="#">dwhitfield@example.net</a>
      </address>
    </div>
    <div class="footer-col posts-col">
      <h3>Recent Blog Posts</h3>
      <ul>
        <li><a href="#">Post Title 1 Goes Here</a></li>
        <li><a href="#">Post Title 2 Goes Here</a></li>
        <li><a href="#">Post Title 3 Goes Here</a></li>
        <li><a href="#">Post Title 4 Goes Here</a></li>
      </ul>
    </div>
    <div class="footer-col search-col">
      <h3>Search</h3>
      <div class="search-field">
        <svg width="26" height="26" viewBox="0 0 26 26" aria-hidden="true">
          <circle cx="10.5" cy="10.5" r="7.5" fill="none" stroke="#7b7f84" stroke-width="3.5"/>
          <line x1="16" y1="16" x2="23.5" y2="23.5" stroke="#7b7f84" stroke-width="4.5" stroke-linecap="round"/>
        </svg>
      </div>
    </div>
  </footer>
</body>
</html>
```